New Body Mist 250 ml exclusive

We are excited to embark on a new project to design the packaging for body mist:
Lunar Bramble

We are looking for a design that is truly unique and stands out, with a touch of individuality that sets it apart. The design should be eye-catching and visually appealing, drawing attention even from a distance. We want the body mists to have a fun and attractive look that appeals to customers.

To help bring your design to life, we will provide the dimensions of the bottle, which has a capacity of 250ml. The bottle measures 13.3 cm in height and 4.9 cm in diameter (excluding the pump). Additionally, we will also provide the dimensions of the label, which measures 15.1 cm in height and 12.8 cm in width.

We believe that giving you the freedom to put your own unique touch and color choices will help create a truly standout design. We look forward to seeing your creative vision for our body mist.

We shared with you the logo of the body mist and some examples of models that we liked.

Please be informed that the project only includes one design and the remaining three will be completed and paid for through a 1on1 project with the winner of the contest.

Target Market(s)

Supermarket and perfumery stores

Industry/Entity Type

Cosmetics

Font styles to use
Serif

Requirements
Must have
• Uniqueness and attractiveness

```html
<!DOCTYPE html>
<html lang="en">
<head>
<meta charset="utf-8">
<title>Lunar Bramble Body Mist Label</title>
<link rel="stylesheet" href="https://fonts.googleapis.com/css2?family=Allura&family=Playfair+Display:wght@700;800&display=swap">
<style>
  :root {
    --canvas: #ffffff;
    --label-top: #ffffff;
    --label-mid: #f7dbe8;
    --label-low: #f2b9d4;
    --label-base: #eaa0c7;
    --blossom-deep: #e0559a;
    --blossom-soft: #f4b3d1;
    --blossom-haze: #fbe3ee;
    --ink: #b02a55;
  }
  html, body {
    margin: 0;
    padding: 0;
    width: 1200px;
    height: 673px;
    overflow: hidden;
    background: var(--canvas);
  }
  .canvas {
    position: relative;
    width: 1200px;
    height: 673px;
  }
  .label {
    position: absolute;
    left: 303px;
    top: 86px;
    width: 594px;
    height: 501px;
    overflow: hidden;
    background: linear-gradient(180deg,
      var(--label-top) 0%,
      var(--label-top) 38%,
      var(--label-mid) 60%,
      var(--label-low) 85%,
      var(--label-base) 100%);
  }
  .label__blossoms {
    position: absolute;
    left: 0;
    top: 0;
    width: 594px;
    height: 400px;
  }
  .label__title {
    position: absolute;
    left: 0;
    width: 594px;
    text-align: center;
    color: var(--ink);
    margin: 0;
  }
  .label__title-script {
    top: 266px;
    font-family: "Allura", cursive;
    font-size: 78px;
    font-weight: 400;
    line-height: 1;
    padding-left: 0;
  }
  .label__title-main {
    top: 340px;
    font-family: "Playfair Display", serif;
    font-weight: 800;
    font-size: 44px;
    letter-spacing: 0.5px;
    line-height: 1;
  }
  .label__volume {
    position: absolute;
    left: 0;
    top: 470px;
    width: 594px;
    text-align: center;
    font-family: "Playfair Display", serif;
    font-weight: 700;
    font-size: 17px;
    color: var(--ink);
    margin: 0;
  }
</style>
</head>
<body>
  <main class="canvas">
    <section class="label">
      <svg class="label__blossoms" viewBox="0 0 594 400" role="img" aria-label="Cherry blossom branches in pink bloom arching across the top of the label">
        <defs>
          <linearGradient id="blossom-fill" x1="0" y1="0" x2="1" y2="1">
            <stop offset="0" stop-color="var(--blossom-deep)"/>
            <stop offset="0.6" stop-color="var(--blossom-soft)"/>
            <stop offset="1" stop-color="var(--blossom-haze)"/>
          </linearGradient>
          <linearGradient id="blossom-haze" x1="0" y1="0" x2="0" y2="1">
            <stop offset="0" stop-color="var(--blossom-haze)" stop-opacity="0.9"/>
            <stop offset="1" stop-color="var(--blossom-haze)" stop-opacity="0"/>
          </linearGradient>
        </defs>
        <rect x="0" y="0" width="594" height="200" fill="url(#blossom-haze)"/>
        <path d="M0 0 H594 V60 C540 110 470 150 400 170 C330 190 260 180 200 200 C150 220 120 270 80 290 C50 305 20 310 0 300 Z" fill="url(#blossom-fill)" opacity="0.85"/>
      </svg>
      <p class="label__title label__title-script">Lunar</p>
      <h1 class="label__title label__title-main">BRAMBLE</h1>
      <p class="label__volume">250ml</p>
    </section>
  </main>
</body>
</html>
```